Need Business Card for our Indian Grocery Store

Industry/Entity Type

Grocery Store

Contact Information for Business Card

Manoj Baweja
Director

Store Locations:

Kelvindale
482 Elm Parade
P: 03 9172 5843

Ashbury
613 Carlow Road
P: 03 9238 6014

email: kvtmarts@mailnest.example

Requirements
Must have
• Our logo Colours

```html
<!DOCTYPE html>
<html lang="en">
<head>
<meta charset="utf-8">
<title>KVT Marts — Business Card</title>
<link rel="stylesheet" href="https://fonts.googleapis.com/css2?family=Crimson+Text:ital,wght@0,400;0,600;1,400&display=swap">
<style>
  :root {
    --backdrop: #2a2a2a;
    --card-dark-1: #3a3a3a;
    --card-dark-2: #1f1f1f;
    --card-light: #f7f7f7;
    --brand-red: #d71f26;
    --ink: #1e1e1e;
    --ink-soft: #4a4a4a;
  }
  * { box-sizing: border-box; margin: 0; padding: 0; }
  html, body { width: 1200px; height: 997px; overflow: hidden; }
  body {
    background: var(--backdrop);
    font-family: "Crimson Text", Georgia, serif;
    position: relative;
  }
  .card {
    position: absolute;
    width: 540px;
    height: 310px;
    border-radius: 18px;
    left: 330px;
    overflow: hidden;
  }
  .card-front {
    top: 110px;
    background: linear-gradient(135deg, var(--card-dark-1), var(--card-dark-2));
  }
  .front-texture { position: absolute; inset: 0; }
  .front-brand {
    position: absolute; left: 0; right: 0; top: 105px;
    text-align: center;
  }
  .brand-name {
    color: var(--brand-red);
    font-weight: 600;
    font-size: 64px;
    line-height: 1;
    letter-spacing: 1px;
  }
  .brand-tagline {
    display: inline-flex; align-items: center; gap: 10px;
    color: var(--brand-red);
    font-style: italic;
    font-size: 20px;
    margin-top: 8px;
  }
  .brand-tagline::before, .brand-tagline::after {
    content: ""; width: 30px; height: 1px; background: var(--brand-red);
  }
  .card-back {
    top: 540px;
    background: var(--card-light);
  }
  .accent-bar {
    position: absolute; left: 28px; width: 4px; background: var(--brand-red);
  }
  .accent-top { top: 0; height: 80px; }
  .accent-bottom { bottom: 0; height: 40px; }
  .back-brand {
    position: absolute; right: 34px; top: 30px; text-align: center;
  }
  .back-brand .brand-name { font-size: 36px; }
  .back-brand .brand-tagline { font-size: 12px; margin-top: 2px; gap: 6px; }
  .back-brand .brand-tagline::before, .back-brand .brand-tagline::after { width: 18px; }
  .contact { position: absolute; left: 50px; top: 140px; color: var(--ink); }
  .person-name { color: var(--brand-red); font-weight: 600; font-size: 21px; line-height: 1.1; }
  .person-role { color: var(--ink-soft); font-size: 15px; margin-bottom: 14px; }
  .line { display: flex; align-items: center; gap: 8px; font-size: 16px; line-height: 1.6; }
  .icon { width: 14px; height: 14px; flex: none; }
  .store-label { font-weight: 600; text-decoration: underline; text-underline-offset: 3px; }
  .store-address { width: 118px; }
  .store-phone { display: inline-flex; align-items: center; gap: 6px; margin-left: 10px; }
  .email { margin-bottom: 10px; font-size: 15px; }
</style>
</head>
<body>
  <section class="card card-front" aria-label="Card front">
    <div class="front-texture" role="img" aria-label="Faint faceted dark grey background texture"></div>
    <div class="front-brand">
      <div class="brand-name">KVT Marts</div>
      <div class="brand-tagline">Fresh Choice Since 2011</div>
    </div>
  </section>

  <section class="card card-back" aria-label="Card back">
    <span class="accent-bar accent-top"></span>
    <span class="accent-bar accent-bottom"></span>
    <div class="back-brand">
      <div class="brand-name">KVT Marts</div>
      <div class="brand-tagline">Fresh Choice Since 2011</div>
    </div>
    <div class="contact">
      <div class="person-name">Manoj Baweja</div>
      <div class="person-role">Director</div>
      <div class="line email">
        <svg class="icon" viewBox="0 0 14 14"><rect x="1" y="3" width="12" height="8" fill="var(--brand-red)"/><path d="M1 3 L7 8 L13 3" stroke="#fff" fill="none" stroke-width="1"/></svg>
        kvtmarts@mailnest.example
      </div>
      <div class="line">
        <span class="store-label">Kelvindale:</span>
        <span class="store-address">482 Elm Parade</span>
        <span class="store-phone">
          <svg class="icon" viewBox="0 0 14 14"><path d="M1 5 Q7 0 13 5 L11 6.5 L9 5 L5 5 L3 6.5 Z" fill="var(--brand-red)"/><rect x="3" y="7" width="8" height="6" rx="1" fill="var(--brand-red)"/></svg>
          03 9172 5843
        </span>
      </div>
      <div class="line">
        <span class="store-label">Ashbury:</span>
        <span class="store-address">613 Carlow Road</span>
        <span class="store-phone">
          <svg class="icon" viewBox="0 0 14 14"><path d="M1 5 Q7 0 13 5 L11 6.5 L9 5 L5 5 L3 6.5 Z" fill="var(--brand-red)"/><rect x="3" y="7" width="8" height="6" rx="1" fill="var(--brand-red)"/></svg>
          03 9238 6014
        </span>
      </div>
    </div>
  </section>
</body>
</html>
```